Covert current Brochures from PDF to PDF editable, No need to change the format

We have 3 brochures that need to be updated in the template to make the content editable. No need to change the format.

```html
<!DOCTYPE html>
<html lang="en">
<head>
<meta charset="utf-8">
<title>NDIS and HCP Services Brochure</title>
<link rel="stylesheet" href="https://fonts.googleapis.com/css2?family=Archivo+Black&family=Archivo+Narrow:wght@500;600;700&family=Arimo:wght@400;700&family=Tinos:ital@1&display=swap">
<style>
  :root {
    --brand-blue: #372d8f;
    --brand-red: #d43a2b;
    --band-red: #cf3f2a;
    --body-text: #454545;
    --paper: #ffffff;
    --photo-light: #e8eef4;
    --photo-mid: #b9cfe2;
  }
  * { margin: 0; padding: 0; box-sizing: border-box; }
  html, body { width: 1200px; height: 849px; overflow: hidden; background: var(--paper); }
  .spread {
    position: relative; width: 1200px; height: 849px; overflow: hidden;
    background: var(--paper); font-family: "Arimo", Arial, sans-serif; color: var(--body-text);
  }
  .hero-photo {
    position: absolute; left: 5px; top: 4px; width: 594px; height: 180px;
    background: linear-gradient(100deg, #d9c2b0 0%, var(--photo-mid) 35%, var(--photo-light) 70%, #f4f4f4 100%);
  }
  .section-title {
    font-family: "Archivo Black", "Arial Black", sans-serif; color: var(--brand-blue);
    letter-spacing: 0.6px; text-transform: uppercase;
  }
  .intro-title { position: absolute; left: 42px; top: 204px; font-size: 16px; line-height: 21px; }
  .body-copy { font-size: 12.8px; line-height: 15.4px; }
  .intro-ndis { position: absolute; left: 40px; top: 270px; width: 255px; }
  .intro-hcp { position: absolute; left: 314px; top: 201px; width: 245px; }

  .blue-band { position: absolute; left: 0; top: 464px; width: 602px; height: 385px; background: var(--brand-blue); }
  .testimonial {
    position: absolute; left: 39px; top: 426px; width: 524px; height: 105px;
    background: var(--paper); border: 2px solid var(--brand-red); padding: 5px 20px 0 20px;
  }
  .testimonial h2 { font-size: 16px; line-height: 20px; text-align: center; margin-bottom: 2px; }
  .testimonial blockquote {
    font-family: "Tinos", "Times New Roman", serif; font-style: italic;
    color: var(--brand-red); font-size: 14.6px; line-height: 19.5px;
  }
  .help-tab {
    position: absolute; left: 3px; top: 547px; width: 291px; height: 32px;
    background: var(--paper); padding: 5px 0 0 38px; font-size: 16.2px;
  }
  .help-lead { position: absolute; left: 40px; top: 591px; color: var(--paper); font-size: 14.2px; }
  .ndis-list { list-style: none; color: var(--paper); position: absolute; }
  .ndis-list li { position: relative; padding-left: 22px; }
  .ndis-list li.bullet::before {
    content: ""; position: absolute; left: 0; top: 4px; width: 10px; height: 10px; background: var(--paper);
  }
  .ndis-list h3 { font-family: "Arimo", Arial, sans-serif; font-weight: 700; font-size: 14px; line-height: 16px; margin-bottom: 3px; }
  .ndis-list p { font-family: "Archivo Narrow", "Arial Narrow", sans-serif; font-weight: 600; font-size: 13.2px; line-height: 13.9px; }
  .list-left { left: 38px; top: 626px; width: 262px; }
  .list-left li:first-child { margin-bottom: 10px; }
  .list-right { left: 319px; top: 555px; width: 240px; }
  .list-right li.continued { margin-bottom: 13px; }
  .list-right li.accommodation { margin-bottom: 8px; }

  .hcp-title { position: absolute; left: 602px; top: 36px; width: 594px; text-align: center; font-size: 16.4px; line-height: 21px; }
  .service { position: absolute; }
  .service h3 { color: var(--brand-red); font-size: 14px; font-weight: 700; line-height: 17px; margin-bottom: 3px; letter-spacing: 0.2px; }
  .service p { font-size: 12.8px; line-height: 15.4px; }
  .col-a { left: 631px; width: 265px; }
  .col-b { left: 913px; width: 262px; }

  .allied-band {
    position: absolute; left: 602px; top: 724px; width: 598px; height: 125px;
    background: var(--band-red); color: var(--paper); padding: 11px 24px 0 32px;
  }
  .allied-band h3 { font-size: 14px; font-weight: 700; line-height: 17px; margin-bottom: 4px; }
  .allied-band p { font-family: "Archivo Narrow", "Arial Narrow", sans-serif; font-weight: 600; font-size: 14.4px; line-height: 15.5px; }
</style>
</head>
<body>
<main class="spread">
  <div class="hero-photo" role="img" aria-label="Photo of a smiling nurse in blue scrubs caring for an elderly white-haired man"></div>

  <h2 class="section-title intro-title">What are NDIS<br>and HCP?</h2>
  <p class="body-copy intro-ndis">The National Disability insurance Scheme (NDIS) is an initiative of the Australian Government that’s managed by the National Disability Insurance Agency (NDIA). Its main goal is to provide lifelong support to individuals with disabilities and enable them to access the necessary services</p>
  <p class="body-copy intro-hcp">On the other hand, Home Care Packages (HCP) provide a cost-effective and flexible way for older Australians to access the care and support they need to remain living in their own homes. These packages are designed to cater to the specific needs of individuals who require more complex care than what is provided by the Commonwealth Home Support Programme. These packages are funded by the Australian government and are administered by approved home care providers.</p>

  <div class="blue-band"></div>

  <section class="testimonial">
    <h2 class="section-title">Testimonials</h2>
    <blockquote>Example Home Care is a great choice. The carers are available 24/7 and very passionate about the resident in helping any situation. I am very happy with their beautiful service.</blockquote>
  </section>

  <h2 class="section-title help-tab">How we can help</h2>
  <p class="help-lead">AS A REGISTERED NDIS PROVIDER:</p>

  <ul class="ndis-list list-left">
    <li class="bullet">
      <h3>In-Home Support</h3>
      <p>We offer a range of in-home support services to help our clients maintain their independence and stay in the comfort of their own homes. Our experienced and compassionate team provides assistance with daily activities such as personal care, medication management, and household chores.</p>
    </li>
    <li class="bullet">
      <h3>Social and Community Integration</h3>
      <p>Our social and community integration services help our clients stay connected to</p>
    </li>
  </ul>

  <ul class="ndis-list list-right">
    <li class="continued">
      <p>their communities and enjoy meaningful activities. From outings to the park, art classes and group activities, we work with our clients to find activities that they enjoy.</p>
    </li>
    <li class="bullet accommodation">
      <h3>Accommodation</h3>
      <p>Short-Term Accommodation (STA), Medium-Term Accommodation (MTA), Supported Independent Living (SIL), 24/7 Care and Private Care.</p>
    </li>
    <li class="bullet">
      <h3>Day Program Centre</h3>
      <p>With a range of activities and programs designed to promote physical, emotional, and cognitive well-being, our centre is the perfect place for those who need additional support or respite care.</p>
    </li>
  </ul>

  <h2 class="section-title hcp-title">As an HCP provider, we can help you and your<br>elderly loved ones with:</h2>

  <section class="service col-a" style="top:106px">
    <h3>Personal Care</h3>
    <p>Our trained and experienced caregivers offer one-on-one assistance with a range of activities of daily living, including bathing, washing, grooming, dressing, walking, toileting, and incontinence care. These tasks can be challenging for elders, but our caregivers approach each task with compassion while maintaining our client’s privacy and independence in their own homes.</p>
  </section>
  <section class="service col-a" style="top:294px">
    <h3>Domestic Assistance</h3>
    <p>Our hands-on domestic assistance helps with everyday household tasks, including dishwashing, cleaning, laundry, grocery shopping, and paying<br>bills. Whether our clients need assistance with light housekeeping tasks or more intensive cleaning, we are here to help.</p>
  </section>
  <section class="service col-a" style="top:434px">
    <h3>Centre-based Respite</h3>
    <p>Caring for a loved one can be both rewarding and challenging, and it’s important to take care of your own health and well-being to continue providing quality care. Our Centre-based Respite Program provides a much-needed break for family members, while also offering an engaging and social environment for their loved ones.</p>
  </section>
  <section class="service col-a" style="top:587px">
    <h3>Meal Assistance</h3>
    <p>Our team provides assistance with meal preparation and feeding to ensure that our clients receive nutritious and delicious meals that meet their dietary requirements and preferences. In addition to meal preparation, our caregivers also provide assistance with feeding, as needed.</p>
  </section>

  <section class="service col-b" style="top:105px">
    <h3>Transportation</h3>
    <p>Transportation can be a significant challenge for seniors, particularly those who are no longer able to drive or who have mobility issues. Our transportation support service is designed to provide safe and reliable transportation for seniors to attend important appointments, stay connected with their communities, and avoid social isolation.</p>
  </section>
  <section class="service col-b" style="top:261px">
    <h3>Flexible Respite</h3>
    <p>We offer flexible respite services to provide carers or family members with the support they need when they need it. Whether you need a few hours to run errands, a weekend break, or an extended holiday, we are here to provide the support you need.</p>
  </section>
  <section class="service col-b" style="top:385px">
    <h3>Social Support</h3>
    <p>Our Social Support service is designed to provide constant companionship and help seniors connect with people and activities that bring them joy and fulfilment. This includes companionship, conversation, and assistance with activities that promote social engagement, such as attending community events and staying connected with family and friends.</p>
  </section>
  <section class="service col-b" style="top:552px">
    <h3>Nursing</h3>
    <p>Our nursing service provides specialized care and support for seniors with a range of medical needs. Our nurses are trained in a variety of specialized areas, including IV therapy, wound care, palliative care, dementia care, and medication administration.</p>
  </section>

  <section class="allied-band">
    <h3>Nursing</h3>
    <p>Our Allied Health and Therapy service is designed to provide seniors with access to the care they need in the comfort and convenience of their own homes. Our skilled and experienced professionals are trained in a variety of specialized areas, including physical therapy, Occupational therapy, speech therapy, and more.</p>
  </section>
</main>
</body>
</html>
```